Business card for a plastic surgeon

i need a business card for a plastic surgeon. I have two adresses. The card should communicate safety, simmetry, beauty and with soft colors.
What i want in the card:
- my logo: Letters "R"and "B" (picture uploaded)
- my name: Renato Bastiani
- my registration: CRM 507 219
- my adresses and phone numbers (2):
- Av Dr Teixeira Lopes, 2710, sala 305 - Vila Olímpia | São Paulo/ SP - Phone: 11 4172-5036
- Al. Itapeva, 47, 3 andar - Alphaville | Barueri/ SP - Phone: 11 6350-2481

- my social network: site, facebook and instagram

Target Market(s)

people (95% girls and women) that want cosmetic procedures and plastic surgery

Industry/Entity Type

Business

Contact Information for Business Card

The card should communicate safety, simmetry, beauty and with soft colors.
Beige, brown, gray, rosy are some options. Color is free

Font styles to use
Serif

Requirements
Must have
• - my logo: Letters "R"and "B" (picture uploaded)
• - my name: Renato Bastiani
• - my registration: CRM 507 219
• - my adresses and phone numbers (2):
• - Av Dr Teixeira Lopes, 2710, sala 305 - Vila Olímpia | São Paulo/ SP - Phone: 11 4172-5036
• - Al. Itapeva, 47, 3 andar - Alphaville | Barueri/ SP - Phone: 11 6350-2481
• - my social network: site, facebook and instagram
Should not have
• other images (only my logo)

```html
<!DOCTYPE html>
<html lang="pt-BR">
<head>
<meta charset="utf-8">
<title>Dr. Renato Bastiani — Cartão de visita</title>
<link rel="stylesheet" href="https://fonts.googleapis.com/css2?family=Cinzel:wght@400;500&family=Open+Sans:wght@400;600&display=swap">
<style>
  :root {
    --backdrop: #ecebe8;
    --kraft: #a89279;
    --kraft-ink: #2e2924;
    --paper: #ffffff;
    --gold: #9d876b;
    --ink: #1f1f1f;
    --shadow: rgba(60, 45, 30, 0.18);
  }
  * { margin: 0; padding: 0; box-sizing: border-box; }
  html, body { width: 1200px; height: 801px; overflow: hidden; background: var(--backdrop); }
  .canvas {
    width: 1200px; height: 801px;
    display: flex; align-items: center; justify-content: center; gap: 60px;
  }
  .card {
    width: 520px; height: 297px;
    position: relative;
    box-shadow: 0 10px 24px var(--shadow);
  }
  .card--front { background: var(--kraft); color: var(--kraft-ink); }
  .card--back { background: var(--paper); color: var(--ink); }

  .brand { font-family: "Cinzel", serif; text-align: center; }
  .brand__mark {
    display: block; margin: 0 auto 14px;
    width: 46px; height: 46px; border-radius: 50%;
    border: 1.5px solid currentColor;
  }
  .brand__name { font-size: 25px; font-weight: 500; letter-spacing: 0.5px; line-height: 1; white-space: nowrap; }
  .brand__role { font-size: 11.5px; letter-spacing: 6px; margin-top: 4px; white-space: nowrap; }

  .card--front .brand { position: absolute; left: 0; right: 0; top: 82px; }

  .card--back .brand {
    position: absolute; left: 30px; top: 108px; color: var(--gold); text-align: left;
  }
  .card--back .brand__name { font-size: 20px; font-weight: 400; }
  .card--back .brand__role { font-size: 9.5px; letter-spacing: 5px; }
  .registration {
    font-family: "Open Sans", sans-serif; font-size: 12px; color: var(--ink);
    margin-top: 8px; padding-left: 62px;
  }

  .contacts {
    position: absolute; left: 270px; top: 92px;
    font-family: "Open Sans", sans-serif; font-size: 12.5px; line-height: 1.4;
  }
  .office { margin-bottom: 20px; }
  .office__row { display: flex; align-items: flex-start; gap: 8px; }
  .office__row svg { flex: none; margin-top: 2px; fill: var(--gold); }
  .office__row--phone { margin-top: 2px; }

  .social { position: absolute; right: 30px; bottom: 26px; display: flex; gap: 12px; }
  .social__item { width: 20px; height: 20px; background: var(--gold); border-radius: 3px; }
</style>
</head>
<body>
<main class="canvas">
  <section class="card card--front">
    <div class="brand">
      <span class="brand__mark" aria-hidden="true"></span>
      <div class="brand__name">DR. RENATO BASTIANI</div>
      <div class="brand__role">CIRURGIÃO PLÁSTICO</div>
    </div>
  </section>

  <section class="card card--back">
    <div class="brand">
      <div class="brand__name">DR. RENATO BASTIANI</div>
      <div class="brand__role">CIRURGIÃO PLÁSTICO</div>
      <div class="registration">CRM 507 219</div>
    </div>

    <div class="contacts">
      <div class="office">
        <div class="office__row">
          <svg width="12" height="15" viewBox="0 0 12 15"><path d="M6 0a6 6 0 0 0-6 6c0 4.2 6 9 6 9s6-4.8 6-9a6 6 0 0 0-6-6zm0 8.3A2.3 2.3 0 1 1 6 3.7a2.3 2.3 0 0 1 0 4.6z"/></svg>
          <span>Av Dr Teixeira Lopes, 2710,<br>sala 305 - Vila Olímpia | São Paulo/ SP</span>
        </div>
        <div class="office__row office__row--phone">
          <svg width="14" height="12" viewBox="0 0 14 12"><path d="M1 3.5C1 1.5 4 1 7 1s6 .5 6 2.5V5h-3V3.5H4V5H1zM3 6h8l2 5H1z"/></svg>
          <span>11 4172-5036</span>
        </div>
      </div>
      <div class="office">
        <div class="office__row">
          <svg width="12" height="15" viewBox="0 0 12 15"><path d="M6 0a6 6 0 0 0-6 6c0 4.2 6 9 6 9s6-4.8 6-9a6 6 0 0 0-6-6zm0 8.3A2.3 2.3 0 1 1 6 3.7a2.3 2.3 0 0 1 0 4.6z"/></svg>
          <span>Al. Itapeva, 47, 3 andar<br>Alphaville | Barueri/ SP</span>
        </div>
        <div class="office__row office__row--phone">
          <svg width="14" height="12" viewBox="0 0 14 12"><path d="M1 3.5C1 1.5 4 1 7 1s6 .5 6 2.5V5h-3V3.5H4V5H1zM3 6h8l2 5H1z"/></svg>
          <span>11 6350-2481</span>
        </div>
      </div>
    </div>

    <div class="social" aria-label="Redes sociais">
      <span class="social__item"></span>
      <span class="social__item"></span>
    </div>
  </section>
</main>
</body>
</html>
```